Document Processing Services and Solutions for School Systems

I am looking to design a brochure for both Digital and Paper use. I can supply the written content. Would be looking for an overall design of the brochure with provided content worked into it.

```html
<!DOCTYPE html>
<html lang="en">
<head>
<meta charset="utf-8">
<title>Northgate Systems – School Document Management Brochure</title>
<link href="https://fonts.googleapis.com/css2?family=Archivo+Black&family=Poppins:wght@400;500;600;700&display=swap" rel="stylesheet">
<style>
:root{
  --blue:#2e2f9a;
  --blue-deep:#24257f;
  --gold:#c9a012;
  --gold-soft:#d9b53a;
  --ink:#1d1d1b;
  --paper:#ffffff;
  --card:#e2e2e2;
  --bg:#ababab;
}
*{margin:0;padding:0;box-sizing:border-box}
html,body{width:724px;height:1200px;overflow:hidden}
body{background:var(--bg);font-family:"Poppins",sans-serif;color:var(--ink);position:relative}
.sheet{position:absolute;left:20px;width:684px;height:264px;overflow:hidden;box-shadow:0 2px 6px rgba(0,0,0,.25)}
.sheet--outside{top:300px}
.sheet--inside{top:630px}
.spread{position:absolute;left:0;top:0;width:1258px;height:486px;background:var(--paper);transform:scale(.5437);transform-origin:0 0}
.abs{position:absolute}
.shapes{position:absolute;left:0;top:0}
.brand{position:absolute;display:flex;align-items:center;gap:8px;font-family:"Poppins",sans-serif;font-weight:700;color:var(--blue);white-space:nowrap}
.display{font-family:"Archivo Black",sans-serif;line-height:1}
.gold{color:var(--gold)}
.blue{color:var(--blue)}

/* outside */
.cta{left:114px;top:112px;color:#fff}
.cta__title{font-size:24px;line-height:1.05}
.cta__sub{font-size:12px;margin-top:12px;line-height:1.3}
.cta__sub b{font-weight:600}
.contact{left:352px;top:0;width:200px;text-align:center}
.contact .brand{position:static;justify-content:center;font-size:21px;margin-top:78px;line-height:30px}
.contact__lead{font-weight:600;font-size:13px;margin-top:14px;letter-spacing:.3px;line-height:18px}
.contact__free{font-size:56px;color:var(--gold);margin-top:2px}
.contact__consult{font-size:18px;color:var(--blue);margin-top:2px}
.contact__text{font-size:12px;line-height:15px;margin-top:10px}
.contact__item{margin-top:10px;font-size:12px;line-height:18px}
.contact__icon{display:block;margin:0 auto 4px}
.cover{left:688px;top:0;width:330px}
.cover .brand{position:static;font-size:27px;margin-top:70px}
.cover__kicker{font-size:15px;letter-spacing:2px;margin-top:34px}
.cover__h{font-size:37px}
.cover__h--1{color:var(--blue);margin-top:2px}
.cover__h--2{color:var(--gold)}
.cover__h--3{color:var(--ink);font-size:30px}
.cover__with{font-size:13px;margin-top:2px}
.cover__with b{font-weight:600}
.pillbar{position:absolute;left:688px;top:300px;height:28px;display:flex;align-items:center;color:#fff;font-weight:500;font-size:14px}
.pillbar span{padding:0 12px 0 8px;border-right:1px solid rgba(255,255,255,.5);display:flex;align-items:center;gap:5px}
.pillbar span:last-child{border:none}
.pillbar i{width:6px;height:6px;border-radius:50%;background:#fff;display:inline-block}
.cover__body{position:absolute;left:688px;top:342px;width:320px;font-size:9.6px;line-height:1.2}
.cover__web{position:absolute;left:688px;top:424px;font-size:15px;letter-spacing:.6px}
.cover__web b{color:var(--blue);font-weight:600}

/* inside */
.sec-title{font-family:"Archivo Black",sans-serif;font-size:18px;color:#fff;left:56px;top:40px}
.why-title{font-family:"Archivo Black",sans-serif;font-size:18px;color:var(--blue);left:688px;top:38px}
.services{left:56px;top:104px;width:380px}
.service{margin-bottom:14px}
.service__head{display:flex;align-items:center;gap:10px;font-weight:600;font-size:10.5px}
.service ul{list-style:none;margin:8px 0 0 34px}
.service li{font-size:7.6px;font-weight:500;line-height:1.25;margin-bottom:7px;padding-left:12px;position:relative}
.service li::before{content:"";position:absolute;left:0;top:1px;width:7px;height:7px;border-radius:50%;background:var(--gold)}
.thumb{position:absolute;left:456px;width:94px;height:88px;border:2px solid #fff;box-shadow:0 1px 4px rgba(0,0,0,.35)}
.thumb svg{display:block}
.footer-url{position:absolute;display:flex;align-items:center;gap:8px;color:#fff;font-size:11px}
.badge{width:18px;height:18px;background:var(--gold);transform:rotate(45deg);display:flex;align-items:center;justify-content:center;border:1.5px solid #fff}
.badge b{transform:rotate(-45deg);font-size:7px;font-weight:600;color:#fff}
.card{position:absolute;width:124px;height:122px;background:var(--card);text-align:center;padding-top:32px}
.card__icon{position:absolute;left:46px;top:-26px}
.card__title{font-weight:600;font-size:8.5px;line-height:1.15}
.card__text{font-size:7px;line-height:1.2;margin-top:4px;padding:0 14px}
</style>
</head>
<body>
<svg width="0" height="0" style="position:absolute" aria-hidden="true">
  <defs>
    <linearGradient id="photoTone" x1="0" y1="0" x2="1" y2="1">
      <stop offset="0" stop-color="#c6c9d0"/>
      <stop offset="1" stop-color="#868a96"/>
    </linearGradient>
    <linearGradient id="goldTone" x1="0" y1="0" x2="1" y2="1">
      <stop offset="0" stop-color="#d4ab22"/>
      <stop offset="1" stop-color="#b68f0c"/>
    </linearGradient>
  </defs>
</svg>

<section class="sheet sheet--outside">
  <div class="spread">
    <svg class="shapes" width="1258" height="486" viewBox="0 0 1258 486">
      <polygon points="0,0 190,0 0,190" fill="url(#goldTone)"/>
      <polygon points="0,300 0,486 190,486" fill="url(#goldTone)"/>
      <rect x="45" y="120" width="260" height="260" rx="34" transform="rotate(45 175 250)" fill="var(--blue)"/>
      <g role="img" aria-label="Photo of hands sorting a stack of paper files">
        <rect x="105" y="285" width="122" height="122" rx="26" transform="rotate(45 166 346)" fill="url(#photoTone)" stroke="#fff" stroke-width="3"/>
      </g>
      <polygon points="1092,0 1258,0 1258,160" fill="var(--blue)"/>
      <polygon points="1200,0 1258,0 1258,50" fill="var(--gold)"/>
      <polygon points="1098,486 1258,486 1258,330" fill="var(--blue)"/>
      <polygon points="1220,486 1258,486 1258,440" fill="var(--gold)"/>
      <g role="img" aria-label="Photo of two colleagues working together at an office computer">
        <polygon points="1055,58 1215,58 1258,100 1258,400 1230,430 1065,430 940,300 1000,240" fill="url(#photoTone)"/>
      </g>
      <polygon points="688,300 972,300 990,328 688,328" fill="var(--gold)"/>
    </svg>

    <div class="abs cta">
      <div class="display cta__title">GET<br><span class="gold">STARTED<br>TODAY!</span></div>
      <p class="cta__sub"><b>LET US HELP YOU</b><br>Modernize your document<br>processing system.</p>
    </div>

    <div class="abs contact">
      <div class="brand"><span>Northgate Systems</span></div>
      <p class="contact__lead">CONTACT US FOR A</p>
      <div class="display contact__free">FREE</div>
      <div class="display contact__consult">CONSULTATION</div>
      <p class="contact__text">and discover how our<br>solutions can transform<br>your school's document<br>management.</p>
      <div class="contact__item">
        <svg class="contact__icon" width="22" height="22" viewBox="0 0 22 22"><rect x="4" y="4" width="14" height="14" transform="rotate(45 11 11)" fill="var(--blue)"/><path d="M8 7c1 3 3 6 6 8l1.5-1.5-2-1.5-1 1c-1-.6-2-1.8-2.5-2.7l1-1-1.4-2z" fill="#fff"/></svg>
        555-014-2290
      </div>
      <div class="contact__item">
        <svg class="contact__icon" width="22" height="22" viewBox="0 0 22 22"><rect x="4" y="4" width="14" height="14" transform="rotate(45 11 11)" fill="var(--blue)"/><rect x="7" y="8" width="8" height="6" fill="none" stroke="#fff" stroke-width="1.2"/><path d="M7 8l4 3 4-3" fill="none" stroke="#fff" stroke-width="1.2"/></svg>
        hello@northgatesys.com
      </div>
      <div class="contact__item">
        <svg class="contact__icon" width="22" height="22" viewBox="0 0 22 22"><rect x="4" y="4" width="14" height="14" transform="rotate(45 11 11)" fill="var(--blue)"/><circle cx="11" cy="11" r="4" fill="none" stroke="#fff" stroke-width="1.1"/><path d="M7 11h8M11 7c-2 2.5-2 5.5 0 8M11 7c2 2.5 2 5.5 0 8" fill="none" stroke="#fff" stroke-width="1"/></svg>
        www.northgatesys.com
      </div>
    </div>

    <div class="abs cover">
      <div class="brand"><span>Northgate Systems</span></div>
      <p class="cover__kicker">Transform Your</p>
      <div class="display cover__h cover__h--1">SCHOOL'S</div>
      <div class="display cover__h cover__h--2">DOCUMENT</div>
      <div class="display cover__h cover__h--3">MANAGEMENT</div>
      <p class="cover__with">with Our <b>Comprehensive Solutions</b></p>
    </div>
    <div class="pillbar"><span><i></i>Streamline</span><span><i></i>Secure</span><span><i></i>Simplify</span></div>
    <p class="cover__body">Managing school documents efficiently is crucial for smooth operations, compliance, and productivity. Our document processing services provide innovative solutions tailored for educational institutions, ensuring secure and seamless document and data handling.</p>
    <p class="cover__web">www.<b>northgatesys</b>.com</p>
  </div>
</section>

<section class="sheet sheet--inside">
  <div class="spread">
    <svg class="shapes" width="1258" height="486" viewBox="0 0 1258 486">
      <rect x="0" y="0" width="1258" height="10" fill="var(--blue)"/>
      <polygon points="0,0 330,0 260,76 0,76" fill="var(--blue)"/>
      <line x1="270" y1="84" x2="340" y2="10" stroke="#ccc" stroke-width="1"/>
      <rect x="0" y="478" width="1258" height="8" fill="var(--blue)"/>
      <polygon points="1160,10 1258,10 1258,110" fill="url(#goldTone)"/>
      <polygon points="1185,320 1258,320 1258,440 1150,440" fill="url(#goldTone)"/>
      <g role="img" aria-label="Photo collage of a business team, a city skyline and hands on a laptop">
        <polygon points="1080,58 1258,58 1258,390 1180,420 1040,330 1040,90" fill="url(#photoTone)"/>
        <rect x="985" y="48" width="120" height="120" rx="26" transform="rotate(45 1045 108)" fill="#a9aab6" stroke="#fff" stroke-width="3"/>
        <rect x="985" y="275" width="120" height="120" rx="26" transform="rotate(45 1045 335)" fill="#b6b8c1" stroke="#fff" stroke-width="3"/>
      </g>
      <polygon points="1000,428 1258,428 1258,486 940,486" fill="var(--blue)"/>
      <polygon points="380,420 560,420 550,446 360,446" fill="var(--blue)"/>
      <line x1="170" y1="433" x2="380" y2="433" stroke="#ccc"/>
      <line x1="796" y1="433" x2="990" y2="433" stroke="#ccc"/>
    </svg>

    <h2 class="abs sec-title">OUR <span class="gold">SERVICES</span></h2>
    <h2 class="abs why-title">WHY <span class="gold">CHOOSE US?</span></h2>

    <div class="abs services">
      <div class="service">
        <div class="service__head"><svg width="24" height="24" viewBox="0 0 24 24"><rect x="5" y="5" width="14" height="14" transform="rotate(45 12 12)" fill="var(--blue)" stroke="var(--gold)" stroke-width="2"/></svg>DOCUMENT SCANNING &amp; CONVERSION</div>
        <ul>
          <li>Convert paper records into digital formats for easy access and storage.</li>
          <li>High-speed scanning for student records, administrative files,<br>and historical archives.</li>
          <li>OCR (Optical Character Recognition) for searchable and editable documents.</li>
        </ul>
      </div>
      <div class="service">
        <div class="service__head"><svg width="24" height="24" viewBox="0 0 24 24"><rect x="5" y="5" width="14" height="14" transform="rotate(45 12 12)" fill="var(--blue)" stroke="var(--gold)" stroke-width="2"/></svg>CLOUD-BASED DOCUMENT MANAGEMENT</div>
        <ul>
          <li>Secure, centralized document storage accessible from anywhere.</li>
          <li>Role-based access controls for administrators, teachers, and staff.</li>
          <li>Automated backups and compliance with educational data<br>security standards.</li>
        </ul>
      </div>
      <div class="service">
        <div class="service__head"><svg width="24" height="24" viewBox="0 0 24 24"><rect x="5" y="5" width="14" height="14" transform="rotate(45 12 12)" fill="var(--blue)" stroke="var(--gold)" stroke-width="2"/></svg>WORKFLOW AUTOMATION</div>
        <ul>
          <li>Digitize and streamline approval processes for enrollment,<br>transcripts, and HR forms.</li>
          <li>Reduce paperwork and improve efficiency with automated workflows.</li>
          <li>Integration capable with existing school management systems.</li>
        </ul>
      </div>
    </div>

    <div class="thumb" style="top:105px" role="img" aria-label="Photo of a person using an office scanner"><svg width="90" height="84"><rect width="90" height="84" fill="url(#photoTone)"/></svg></div>
    <div class="thumb" style="top:202px" role="img" aria-label="Illustration of cloud storage above an open hand"><svg width="90" height="84"><rect width="90" height="84" fill="url(#photoTone)"/></svg></div>
    <div class="thumb" style="top:300px" role="img" aria-label="Photo of staff working at computer screens"><svg width="90" height="84"><rect width="90" height="84" fill="url(#photoTone)"/></svg></div>

    <div class="brand" style="left:55px;top:422px;font-size:18px"><span>Northgate Systems</span></div>
    <div class="footer-url" style="left:400px;top:424px">www.northgatesys.com<span class="badge"><b>01</b></span></div>

    <div class="card" style="left:688px;top:100px">
      <svg class="card__icon" width="32" height="32" viewBox="0 0 32 32"><rect x="7" y="7" width="18" height="18" transform="rotate(45 16 16)" fill="var(--blue)" stroke="var(--gold)" stroke-width="2.5"/><path d="M11 20l4-4 3 2 4-5" fill="none" stroke="#fff" stroke-width="1.6"/></svg>
      <p class="card__title">INCREASED<br>EFFICIENCY</p>
      <p class="card__text">Save time with digital workflows and instant document retrieval.</p>
    </div>
    <div class="card" style="left:822px;top:100px">
      <svg class="card__icon" width="32" height="32" viewBox="0 0 32 32"><rect x="7" y="7" width="18" height="18" transform="rotate(45 16 16)" fill="var(--blue)" stroke="var(--gold)" stroke-width="2.5"/><rect x="12" y="15" width="8" height="6" fill="#fff"/><path d="M13.5 15v-2a2.5 2.5 0 0 1 5 0v2" fill="none" stroke="#fff" stroke-width="1.4"/></svg>
      <p class="card__title">ENHANCED<br>SECURITY</p>
      <p class="card__text">Protect sensitive student and faculty information.</p>
    </div>
    <div class="card" style="left:688px;top:265px">
      <svg class="card__icon" width="32" height="32" viewBox="0 0 32 32"><rect x="7" y="7" width="18" height="18" transform="rotate(45 16 16)" fill="var(--blue)" stroke="var(--gold)" stroke-width="2.5"/><circle cx="16" cy="16" r="4.5" fill="none" stroke="#fff" stroke-width="1.6"/></svg>
      <p class="card__title">COST<br>SAVINGS</p>
      <p class="card__text">Reduce paper, printing, and storage costs.</p>
    </div>
    <div class="card" style="left:822px;top:265px">
      <svg class="card__icon" width="32" height="32" viewBox="0 0 32 32"><rect x="7" y="7" width="18" height="18" transform="rotate(45 16 16)" fill="var(--blue)" stroke="var(--gold)" stroke-width="2.5"/><path d="M12 20c0-5 3-8 8-8 0 5-3 8-8 8z" fill="#fff"/></svg>
      <p class="card__title">ECO<br>FRIENDLY</p>
      <p class="card__text">Minimize your school's carbon footprint by going digital.</p>
    </div>

    <div class="brand" style="left:688px;top:422px;font-size:18px"><span>Northgate Systems</span></div>
    <div class="footer-url" style="left:1034px;top:444px">www.northgatesys.com<span class="badge"><b>02</b></span></div>
  </div>
</section>
</body>
</html>
```